National hospice pharmacy network needs a powerpoint design

We need a power point design for a new company that is creating a network of independent pharmacies to provide medication delivery to hospice patients in their area. We will be providing them with logistics to build a delivery system, software to increase efficiency and the marketing to hospice agencies. The pharmacies will benefit with increasing their patient care, increasing their efficiency and increasing their profits.

Pharmacy

```html
<!DOCTYPE html>
<html lang="en">
<head>
<meta charset="utf-8">
<title>MedReach – Presentation Slides</title>
<link rel="stylesheet" href="https://fonts.googleapis.com/css2?family=Fenix&family=Cormorant+Garamond:ital,wght@1,400&display=swap">
<style>
  :root {
    --backdrop: #707175;
    --slide: #ffffff;
    --shadow: rgba(0,0,0,0.75);
    --brand-blue: #2a5aa6;
    --brand-green: #3db04b;
    --ink: #1b1b1b;
    --ink-soft: #4a4a4a;
  }
  * { margin: 0; padding: 0; box-sizing: border-box; }
  html, body { width: 847px; height: 1200px; overflow: hidden; }
  body {
    background: var(--backdrop);
    position: relative;
    font-family: "Fenix", Georgia, serif;
    color: var(--ink);
  }
  .slide {
    position: absolute;
    background: var(--slide);
    box-shadow: 7px 7px 6px var(--shadow);
  }
  .slide--content { left: 91px; top: 75px; width: 664px; height: 498px; }
  .slide--closing { left: 90px; top: 622px; width: 662px; height: 496px; }

  .page-number {
    position: absolute; left: 33px; top: 0; width: 39px; height: 33px;
    background: var(--brand-green); color: #fff;
    font-size: 14px; line-height: 33px; text-align: center;
  }
  .slide-title {
    position: absolute; left: 0; right: 0; top: 50px;
    text-align: center;
    font-family: "Cormorant Garamond", Georgia, serif;
    font-style: italic; font-weight: 400; font-size: 28px;
  }
  .point-list { position: absolute; left: 67px; top: 127px; list-style: none; }
  .point { position: relative; padding-left: 29px; font-size: 13px; line-height: 18.5px; }
  .point::before {
    content: "➢"; position: absolute; left: 0; top: 0; font-size: 11px;
  }
  .point-detail {
    list-style: none; padding-left: 29px; color: var(--ink-soft);
  }
  .point-detail li { position: relative; padding-left: 22px; }
  .point-detail li::before { content: "•"; position: absolute; left: 5px; }

  .wordmark {
    position: absolute; color: var(--brand-blue);
    font-family: "Fenix", Georgia, serif; font-weight: 400;
    display: flex; align-items: center; white-space: nowrap;
  }
  .wordmark .dot {
    display: inline-block; border-radius: 50%; background: var(--brand-green);
  }
  .slide--content .wordmark { left: 21px; top: 443px; font-size: 27px; gap: 6px; }
  .slide--content .wordmark .dot { width: 12px; height: 12px; }
  .footer-bar { position: absolute; top: 454px; height: 10px; }
  .footer-bar--blue { left: 155px; width: 249px; background: var(--brand-blue); }
  .footer-bar--green { left: 404px; width: 260px; background: var(--brand-green); }

  .closing-heading {
    position: absolute; left: 320px; width: 312px; text-align: center;
    font-size: 18px;
  }
  .closing-heading--question { top: 58px; }
  .closing-heading--thanks { top: 107px; }
  .slide--closing .wordmark { left: 28px; top: 176px; font-size: 46px; gap: 8px; }
  .slide--closing .wordmark .dot { width: 18px; height: 18px; }
  .divider-line { position: absolute; left: 28px; top: 218px; }
  .contact {
    position: absolute; left: 343px; top: 328px; width: 260px;
    font-size: 15px; line-height: 19px; color: var(--ink-soft);
  }
  .website {
    position: absolute; left: 0; right: 0; top: 461px; text-align: center;
    font-size: 13px; color: var(--ink-soft);
  }
</style>
</head>
<body>
  <section class="slide slide--content">
    <div class="page-number">4</div>
    <h1 class="slide-title">Increased Patient Care</h1>
    <ul class="point-list">
      <li class="point">Local
        <ul class="point-detail"><li>Many hospice patients are forced to use mail order</li></ul>
      </li>
      <li class="point">Fast Delivery
        <ul class="point-detail"><li>Consistent same day delivery</li></ul>
      </li>
      <li class="point">Positive impact
        <ul class="point-detail"><li>Software is intuitive and easily fits around any pharmacy work flow</li></ul>
      </li>
    </ul>
    <div class="wordmark">MedReach<span class="dot"></span></div>
    <div class="footer-bar footer-bar--blue"></div>
    <div class="footer-bar footer-bar--green"></div>
  </section>

  <section class="slide slide--closing">
    <h2 class="closing-heading closing-heading--question">Question and Concerns</h2>
    <h2 class="closing-heading closing-heading--thanks">Thank you</h2>
    <div class="wordmark">MedReach<span class="dot"></span></div>
    <svg class="divider-line" width="634" height="10" viewBox="0 0 634 10" aria-hidden="true">
      <line x1="0" y1="8" x2="634" y2="3" stroke="#3db04b" stroke-width="2.5"/>
    </svg>
    <p class="contact">Contact us on:- Your contact number comes here. Your address,&nbsp; phone number and fax number <strong>.</strong></p>
    <p class="website">www.Yourwebid.com</p>
  </section>
</body>
</html>
```